Hair Salon Brochure

We need a brochure for our hair salon located in Middle Tennessee called Marla Looks of Harbor Bend. Along with standard services, we offer specialized services and accommodations for individuals on the Autism Spectrum, regardless of background or hair type.
At Marla Looks of Harbor Bend, our mission is to create a warm and inclusive haven for individuals of all backgrounds, including those on the autism spectrum and their families. We are dedicated to providing not only exceptional hairstyling services but also hands-on education and specialized cutting techniques for clients with natural textured hair. Our goal is to empower our clients with the knowledge and tools necessary to maintain a successful hair care routine, ensuring they leave our salon feeling confident.
We believe in fostering a sense of community, where parents of younger clients are encouraged to learn the proper hair care techniques for their children, promoting healthy practices at home. Our commitment extends beyond just hair; we are here to help you embrace your true self and recognize the beauty that resides within.
At Marla Looks of Harbor Bend, our passion is to deliver the ultimate client experience, where you can be unapologetically yourself and feel completely at ease. From the moment you step through our doors, you are welcomed not only to discuss your hair concerns but also to engage in meaningful conversations about life. Together, we will collaborate on a personalized plan to achieve your hair goals and transform the way you perceive yourself.
Always remember, when you look good, you feel good, and when you feel good, you can achieve great things. We firmly believe that every individual is 'Beautiful Beyond the Spectrum,' and we are here to celebrate that beauty with you."
https://www.marlalooksbend.net/
Tagline - "Beautiful Beyond the Spectrum"

```html
<!DOCTYPE html>
<html lang="en">
<head>
<meta charset="utf-8">
<title>Marla Looks of Harbor Bend — Brochure Outside</title>
<link rel="stylesheet" href="https://fonts.googleapis.com/css2?family=Josefin+Sans:ital,wght@0,300;0,400;1,300;1,400&family=Quicksand:wght@400;500&family=Great+Vibes&display=swap">
<style>
  :root {
    --bg: #dcdcdc;
    --paper: #ffffff;
    --brand-blue: #1f6fbd;
    --panel-blue: #1e80d2;
    --panel-blue-deep: #1565b4;
    --ink: #2b2b2b;
    --copper: #c4631f;
    --copper-dark: #3a2414;
    --accent-orange: #e06a2a;
    --owner-purple: #6b2fc4;
  }
  * { box-sizing: border-box; margin: 0; padding: 0; }
  html, body { width: 924px; height: 1200px; overflow: hidden; }
  body {
    background: var(--bg);
    font-family: "Josefin Sans", sans-serif;
    position: relative;
  }
  .brochure {
    position: absolute;
    left: 42px; top: 270px;
    width: 840px; height: 650px;
    display: flex;
    box-shadow: 0 6px 18px rgba(0,0,0,.18);
  }
  .panel { width: 280px; height: 100%; position: relative; overflow: hidden; }

  /* Left panel */
  .panel--about { background: var(--paper); padding: 26px 22px 0; }
  .heading {
    font-family: "Josefin Sans", sans-serif;
    font-style: italic; font-weight: 300;
    color: var(--brand-blue);
    font-size: 19px; line-height: 1.15;
  }
  .body-copy {
    font-style: italic; font-weight: 300;
    font-size: 8.4px; line-height: 1.35;
    color: var(--ink); margin-top: 8px;
  }
  .meet-owner { margin-top: 26px; }
  .meet-owner .heading { font-size: 22px; }
  .owner-photo {
    position: absolute; left: 18px; bottom: 26px;
    width: 120px; height: 150px;
    border-radius: 60px 60px 6px 6px;
    background: linear-gradient(160deg, #6a4632, #2a2220 70%);
  }
  .owner-signature {
    position: absolute; left: 138px; bottom: 70px;
    font-family: "Great Vibes", cursive;
    color: var(--owner-purple); font-size: 30px; line-height: .9;
  }
  .owner-signature small {
    display: block; text-align: right;
    font-family: "Josefin Sans", sans-serif; font-style: italic;
    font-size: 8px; margin-top: 4px;
  }
  .skyline-left {
    position: absolute; left: 0; bottom: 0; width: 180px; height: 24px;
    background: linear-gradient(to top, #e6e6e6, rgba(255,255,255,0));
  }

  /* Middle panel */
  .panel--contact {
    background: linear-gradient(180deg, var(--panel-blue) 0%, var(--panel-blue-deep) 100%);
    color: #fff; text-align: center; padding: 28px 20px 0;
  }
  .testimonials-title {
    font-family: "Quicksand", sans-serif; font-weight: 400;
    font-size: 25px; letter-spacing: .5px;
  }
  .quote-mark { display: block; margin: 4px auto 6px; }
  .testimonial { font-style: italic; font-size: 8.2px; line-height: 1.35; margin-bottom: 6px; }
  .salon-photo {
    width: 136px; height: 136px; border-radius: 50%;
    margin: 16px auto 0; border: 3px solid #fff;
    background: linear-gradient(135deg, #3c7f93, #c2582a 55%, #3a2a26);
  }
  .contact-icons { display: flex; justify-content: center; gap: 8px; margin-top: 20px; }
  .contact-address { font-family: "Quicksand", sans-serif; font-size: 10.5px; line-height: 1.3; margin-top: 8px; }
  .contact-phone { font-family: "Quicksand", sans-serif; font-size: 17px; margin-top: 12px; letter-spacing: 1px; }
  .contact-web { font-family: "Quicksand", sans-serif; font-size: 12px; margin-top: 10px; }
  .skyline-mid {
    position: absolute; left: 0; bottom: 0; width: 100%; height: 44px;
    background: linear-gradient(to top, rgba(255,255,255,.9), rgba(255,255,255,.15));
  }

  /* Right panel: cover */
  .panel--cover { background: var(--paper); text-align: center; }
  .cover-photo {
    height: 300px;
    background: linear-gradient(180deg, var(--copper) 0%, var(--copper-dark) 55%, #b8b8b8 85%, #ffffff 100%);
  }
  .brand-name {
    display: flex; align-items: center; justify-content: center; gap: 10px;
    margin: 30px 20px 0;
    font-family: "Quicksand", sans-serif; font-weight: 500;
    color: var(--brand-blue); font-size: 25px; line-height: 1.15;
  }
  .brand-name .mark { flex: none; width: 18px; height: 18px; border-radius: 50%; background: var(--brand-blue); }
  .tagline {
    font-family: "Quicksand", sans-serif; color: var(--brand-blue);
    font-size: 24px; line-height: 1.15; margin-top: 30px;
  }
  .cover-web {
    display: flex; align-items: center; justify-content: center; gap: 6px;
    margin-top: 26px; font-family: "Quicksand", sans-serif; font-weight: 500;
    font-size: 10px; letter-spacing: 3px; color: var(--brand-blue);
  }
  .cover-web .dot { width: 8px; height: 8px; border-radius: 50%; background: var(--accent-orange); }
</style>
</head>
<body>
<main class="brochure">
  <section class="panel panel--about">
    <h2 class="heading">Get a fresh look in a<br>welcoming environment</h2>
    <p class="body-copy">We create a warm and inclusive haven for everyone, regardless of background or hair type. We offer specialized services and accommodations for individuals on the autism spectrum.</p>
    <p class="body-copy">At Marla Looks of Harbor Bend, our passion is to deliver the ultimate client experience, where you can be unapologetically yourself and feel completely at ease.</p>
    <div class="meet-owner">
      <h2 class="heading">Meet the Owner</h2>
      <p class="body-copy">Dana Whitfield, Owner of Marla Looks of Harbor Bend, proudly hails from the picturesque town of Willow Creek, Tennessee. Since 2002, Dana has held the title of a Licensed Cosmetologist, specializing in crafting personalized and unforgettable hair care experiences. Her journey in the world of beauty has been a profound one, driven by her unwavering passion for Beauty, Education and Self-Love. Dana emphasizes the importance of self-care as a daily ritual, not just an occasional indulgence. It's a philosophy she shares with her clients, nurturing our inner and outer selves for a fulfilling life.</p>
    </div>
    <div class="owner-photo" role="img" aria-label="Portrait photo of the salon owner"></div>
    <p class="owner-signature">Dana<br>Whitfield<small>(Owner)</small></p>
    <div class="skyline-left" role="img" aria-label="City skyline silhouette"></div>
  </section>

  <section class="panel panel--contact">
    <h2 class="testimonials-title">Client Testimonials</h2>
    <svg class="quote-mark" width="18" height="14" viewBox="0 0 18 14" aria-hidden="true">
      <circle cx="4.5" cy="9" r="4" fill="#fff"/><path d="M1 9 Q1 2 7 0" stroke="#fff" stroke-width="2" fill="none"/>
      <circle cx="13.5" cy="9" r="4" fill="#fff"/><path d="M10 9 Q10 2 16 0" stroke="#fff" stroke-width="2" fill="none"/>
    </svg>
    <p class="testimonial">"I was looking for someone with experience cutting curly hair &amp; came across Dana &amp; I am so glad I did! I had a wonderful experience &amp; I love my hair! I told her what I wanted &amp; she really listened and offered great suggestions. I will definitely be back to see Dana!"</p>
    <p class="testimonial">"Dana was so wonderful with my young daughter. She spent two hours (!!) with us teaching us all kinds of new tricks. Her patience and knowledge were top notch. My daughter is so proud of her hair and is taking so much ownership of what she learned. We were so lucky to find Dana!"</p>
    <div class="salon-photo" role="img" aria-label="Photo of the salon interior"></div>
    <div class="contact-icons" aria-hidden="true">
      <svg width="12" height="14" viewBox="0 0 12 14"><circle cx="6" cy="5" r="4" fill="#fff"/><path d="M6 9 L6 14" stroke="#fff" stroke-width="1.5"/></svg>
      <svg width="14" height="14" viewBox="0 0 14 14"><path d="M3 1 L5 4 L4 6 Q6 9 8 10 L10 9 L13 11 L12 13 Q5 13 1 3 Z" fill="#fff"/></svg>
      <svg width="14" height="14" viewBox="0 0 14 14"><circle cx="7" cy="7" r="6" fill="none" stroke="#fff" stroke-width="1.3"/><ellipse cx="7" cy="7" rx="2.6" ry="6" fill="none" stroke="#fff" stroke-width="1"/><path d="M1 7 H13" stroke="#fff" stroke-width="1"/></svg>
    </div>
    <p class="contact-address">Marla Looks of Harbor Bend<br>418 Cedar Hollow Rd Suite 12<br>HARBOR BEND, Tennessee 37000</p>
    <p class="contact-phone">(615) 555-0187</p>
    <p class="contact-web">www.marlalooksbend.net</p>
    <div class="skyline-mid" role="img" aria-label="City skyline silhouette"></div>
  </section>

  <section class="panel panel--cover">
    <div class="cover-photo" role="img" aria-label="Photo of a salon window with blinds and warm lights"></div>
    <h1 class="brand-name"><span class="mark" aria-hidden="true"></span>Marla Looks of Harbor Bend</h1>
    <p class="tagline">Beautiful Beyond<br>the Spectrum</p>
    <p class="cover-web"><span class="dot" aria-hidden="true"></span>www.marlalooksbend.net</p>
  </section>
</main>
</body>
</html>
```